'Our Values' graphic

Hi there,
Could I get few options creating this graphic in a more minimalist, corporate look - using minimalist graphic elements and designs and using minimalist fonts (see tavlix or mundelo for inspiration)
I would also like the lines around the outside to be more minimalist. Maybe a thin line or a graphic element.
Change 'Core Values' title to 'Our Values'
Keep the font of 'Values'.
I would like to see a version in all dark grey and another version with the font in the lower square with each line of font being a different colour (Red, Blue, Green and Orange)

Requirements
Must have
• 'Our Values' and using the same font for 'Values' as the original artwork
Nice to have
• Minimalist artwork

```html
<!DOCTYPE html>
<html lang="en">
<head>
<meta charset="utf-8">
<title>Our Values</title>
<link rel="stylesheet" href="https://fonts.googleapis.com/css2?family=Caveat+Brush&family=Oswald:wght@400;700&display=swap">
<style>
  :root {
    --stage: #e4e5e6;
    --blue: #29a9e0;
    --ink: #333431;
    --white: #ffffff;
    --sky: #a3c4e8;
    --sky-soft: #abdff7;
    --charcoal: #333431;
  }
  html, body {
    margin: 0;
    padding: 0;
    width: 1200px;
    height: 793px;
    overflow: hidden;
    background: var(--stage);
  }
  .canvas {
    position: relative;
    width: 1200px;
    height: 793px;
  }
  .poster {
    position: absolute;
    top: 62px;
    width: 474px;
    height: 669px;
    overflow: hidden;
  }
  .poster--light {
    left: 90px;
    background:
      radial-gradient(ellipse 70% 45% at 0% 0%, var(--sky) 0%, rgba(163,196,232,0) 100%),
      radial-gradient(ellipse 75% 50% at 100% 100%, var(--sky-soft) 0%, rgba(171,223,247,0) 100%),
      var(--white);
    --word: var(--ink);
  }
  .poster--dark {
    left: 644px;
    background: var(--charcoal);
    --word: var(--white);
  }
  .title-values {
    position: absolute;
    left: 232px;
    top: 52px;
    margin: 0;
    font-family: "Caveat Brush", cursive;
    font-size: 92px;
    line-height: 1;
    color: var(--word);
    letter-spacing: -2px;
    white-space: nowrap;
  }
  .title-our {
    position: absolute;
    left: 362px;
    top: 35px;
    margin: 0;
    font-family: "Oswald", sans-serif;
    font-weight: 700;
    font-size: 46px;
    line-height: 1;
    color: var(--blue);
    letter-spacing: -0.5px;
    transform: scaleX(0.82);
    transform-origin: left top;
    white-space: nowrap;
  }
  .value {
    position: absolute;
    left: 0;
    width: 474px;
    height: 100px;
  }
  .value__initial {
    position: absolute;
    left: 44px;
    top: -16px;
    width: 52px;
    text-align: center;
    font-family: "Oswald", sans-serif;
    font-weight: 700;
    font-size: 118px;
    line-height: 1;
    color: var(--blue);
    transform: scaleX(0.9);
    transform-origin: center top;
  }
  .value__lead {
    position: absolute;
    left: 101px;
    top: 7px;
    font-family: "Oswald", sans-serif;
    font-weight: 700;
    font-size: 48px;
    line-height: 1;
    color: var(--blue);
    letter-spacing: -1.5px;
    white-space: nowrap;
  }
  .value__rest {
    position: absolute;
    left: 102px;
    top: 50px;
    font-family: "Oswald", sans-serif;
    font-weight: 400;
    font-size: 49px;
    line-height: 1;
    color: var(--word);
    letter-spacing: -2.8px;
    white-space: nowrap;
  }
  .value--rise { top: 203px; }
  .value--innovate { top: 310px; }
  .value--safety { top: 415px; }
  .value--empower { top: 522px; }
</style>
</head>
<body>
<div class="canvas">
  <section class="poster poster--light">
    <p class="title-values">Values</p>
    <p class="title-our">OUR</p>
    <div class="value value--rise"><span class="value__initial">R</span><span class="value__lead">ISE</span><span class="value__rest">TOGETHER</span></div>
    <div class="value value--innovate"><span class="value__initial">I</span><span class="value__lead">NNOVATE</span><span class="value__rest">EDUCATION</span></div>
    <div class="value value--safety"><span class="value__initial">S</span><span class="value__lead">AFETY</span><span class="value__rest">FIRST</span></div>
    <div class="value value--empower"><span class="value__initial">E</span><span class="value__lead">MPOWER</span><span class="value__rest">CONNECTIONS</span></div>
  </section>

  <section class="poster poster--dark">
    <p class="title-values">Values</p>
    <p class="title-our">OUR</p>
    <div class="value value--rise"><span class="value__initial">R</span><span class="value__lead">ISE</span><span class="value__rest">TOGETHER</span></div>
    <div class="value value--innovate"><span class="value__initial">I</span><span class="value__lead">NNOVATE</span><span class="value__rest">EDUCATION</span></div>
    <div class="value value--safety"><span class="value__initial">S</span><span class="value__lead">AFETY</span><span class="value__rest">FIRST</span></div>
    <div class="value value--empower"><span class="value__initial">E</span><span class="value__lead">MPOWER</span><span class="value__rest">CONNECTIONS</span></div>
  </section>
</div>
</body>
</html>
```